A simple Chatterbook Ad (not Chatterbook Page) for weight loss surgery

It’s a simple ad in terms of the text.

The text should say:
Curious about weight loss surgery?
This 30 second quiz will tell you which procedure will suit you best

I'm open to variations in the text if it is thought to enhance the ad.

Targeted towards obese individuals who have been unable to lose weight with diet and exercise. My industry is weight loss surgery – webpage www.marcusbellweather.com.au. Clicking the ad leads to a quiz on my webpage relating to weight loss surgery. Most frequent users of this service are females (75%) between ages of 35 and 55 years.

Successful weight loss surgery can enable individuals who have been unable to lose weight to lose a substantial amount of the excess weight they are carrying to be healthier and happier.

```html
<!DOCTYPE html>
<html lang="en">
<head>
<meta charset="utf-8">
<title>Weight Loss Surgery Quiz Ad</title>
<link rel="stylesheet" href="https://fonts.googleapis.com/css2?family=Anton&family=Playfair+Display:ital,wght@1,700;1,800&display=swap">
<style>
  :root {
    --navy: #12243a;
    --teal: #45aea6;
    --teal-text: #38a396;
    --white: #ffffff;
    --park-light: #dfe3c4;
    --park-mid: #a9b98a;
    --park-dark: #7f9a62;
    --shirt: #1fa7b8;
  }
  * { margin: 0; padding: 0; box-sizing: border-box; }
  html, body { width: 1200px; height: 1200px; overflow: hidden; background: var(--white); }
  .ad {
    position: relative;
    width: 1200px;
    height: 1200px;
    overflow: hidden;
  }
  .ad__photo {
    position: absolute;
    inset: 0;
    background:
      radial-gradient(ellipse 300px 520px at 930px 640px, var(--shirt) 0%, rgba(31,167,184,0.75) 55%, rgba(31,167,184,0) 100%),
      radial-gradient(ellipse 220px 260px at 960px 1080px, rgba(26,26,31,0.9) 0%, rgba(26,26,31,0) 100%),
      linear-gradient(160deg, var(--park-mid) 0%, var(--park-light) 45%, var(--park-dark) 100%);
  }
  .ad__frame {
    position: absolute;
    left: 61px; top: 61px;
    width: 1078px; height: 1078px;
    border: 14px solid var(--navy);
  }
  .thought {
    position: absolute;
    left: 200px; top: 40px;
    width: 470px; height: 215px;
  }
  .thought__text {
    position: absolute;
    left: 210px; top: 90px;
    width: 350px;
    text-align: center;
    font-family: "Playfair Display", serif;
    font-style: italic;
    font-weight: 700;
    font-size: 37px;
    line-height: 48px;
    color: var(--navy);
  }
  .accent { color: var(--teal-text); }
  .headline__kicker {
    position: absolute;
    left: 68px; top: 298px;
    width: 544px; height: 130px;
    background: var(--teal);
    color: var(--white);
    font-family: "Anton", sans-serif;
    font-size: 82px;
    line-height: 130px;
    padding-left: 36px;
    text-transform: uppercase;
  }
  .headline__main {
    position: absolute;
    left: 68px; top: 428px;
    width: 617px; height: 310px;
    background: var(--navy);
    color: var(--white);
    font-family: "Anton", sans-serif;
    font-size: 108px;
    line-height: 126px;
    padding: 32px 0 0 36px;
    text-transform: uppercase;
  }
  .offer {
    position: absolute;
    left: 68px; top: 738px;
    width: 640px; height: 318px;
    background: linear-gradient(90deg, rgba(240,242,230,0.92) 0%, rgba(240,242,230,0.6) 80%, rgba(240,242,230,0) 100%);
  }
  .offer__text {
    position: absolute;
    left: 100px; top: 762px;
    width: 540px;
    font-family: "Playfair Display", serif;
    font-style: italic;
    font-weight: 800;
    font-size: 56px;
    line-height: 60px;
    color: var(--navy);
  }
  .cursor {
    position: absolute;
    left: 36px; top: 1028px;
    width: 96px; height: 128px;
  }
  .brand {
    position: absolute;
    right: 90px; top: 1050px;
    display: flex;
    align-items: center;
    gap: 10px;
    font-family: "Anton", sans-serif;
    font-size: 26px;
    color: var(--navy);
  }
  .brand__dot {
    width: 22px; height: 22px;
    border-radius: 50%;
    background: var(--teal);
  }
</style>
</head>
<body>
  <main class="ad">
    <div class="ad__photo" role="img" aria-label="Photo of a woman in a teal t-shirt with headphones and a towel around her neck, resting hands on knees after exercise in a sunny park"></div>
    <div class="ad__frame"></div>

    <svg class="thought" viewBox="0 0 470 215" aria-hidden="true">
      <g fill="#ffffff">
        <ellipse cx="180" cy="118" rx="175" ry="72"/>
        <circle cx="95" cy="80" r="55"/>
        <circle cx="175" cy="55" r="60"/>
        <circle cx="265" cy="65" r="55"/>
        <circle cx="310" cy="115" r="50"/>
        <circle cx="250" cy="165" r="45"/>
        <circle cx="130" cy="165" r="45"/>
        <circle cx="45" cy="125" r="42"/>
        <circle cx="398" cy="92" r="25"/>
        <circle cx="445" cy="94" r="13"/>
      </g>
    </svg>
    <p class="thought__text">There has to<br>be a <span class="accent">better</span> way!</p>

    <h1>
      <span class="headline__kicker">Curious about</span>
      <span class="headline__main">Weight loss<br>surgery?</span>
    </h1>

    <div class="offer"></div>
    <p class="offer__text">This <span class="accent">30 second</span> quiz will tell you which procedure will suit you best!</p>

    <svg class="cursor" viewBox="0 0 96 128" aria-hidden="true">
      <path d="M10 8 L10 104 L34 82 L52 120 L70 112 L52 74 L86 72 Z"
            fill="#ffffff" stroke="#12243a" stroke-width="7" stroke-linejoin="round"/>
    </svg>

    <div class="brand"><span class="brand__dot"></span>Northbay Surgical</div>
  </main>
</body>
</html>
```